Business Card Design

I'd like to have some business cards designed using my new logo. I am an accountant and company secretary and offer these services through Holloway Meridian Advisory Pty Ltd. I am the sole Director of the company. Please let me know if you require any further logo files.

Industry/Entity Type

Business

```html
<!DOCTYPE html>
<html lang="en">
<head>
<meta charset="utf-8">
<title>Holloway Meridian Advisory – Business Cards</title>
<link rel="stylesheet" href="https://fonts.googleapis.com/css2?family=Marcellus&display=swap">
<style>
  :root {
    --brand-blue: #1777c2;
    --brand-grey: #6d6e71;
    --page-bg: #f4f4f4;
    --card-white: #fbfbfb;
    --shadow: 0 6px 8px rgba(0,0,0,0.28);
  }
  * { margin: 0; padding: 0; box-sizing: border-box; }
  html, body { width: 1200px; height: 900px; overflow: hidden; }
  body {
    background: var(--page-bg);
    font-family: "Marcellus", "Optima", serif;
    position: relative;
  }
  .card {
    position: absolute;
    width: 400px;
    height: 242px;
    box-shadow: var(--shadow);
    overflow: hidden;
  }
  .card--back { background: var(--brand-blue); }
  .card--front { background: var(--card-white); }

  .card--back-plain  { left: 169px; top: 141px; }
  .card--front-plain { left: 633px; top: 141px; }
  .card--back-swoosh { left: 169px; top: 517px; height: 241px; }
  .card--front-swoosh{ left: 633px; top: 517px; height: 241px; }

  .lockup { position: absolute; display: flex; align-items: center; gap: 14px; }
  .lockup__dot { width: 18px; height: 18px; border-radius: 50%; flex: none; }
  .lockup__name {
    font-size: 12.5px;
    line-height: 13.6px;
    letter-spacing: 0.4px;
    text-transform: uppercase;
  }
  .lockup--light .lockup__dot { background: #fff; }
  .lockup--light .lockup__name { color: #fff; }
  .lockup--dark .lockup__dot { background: var(--brand-blue); }
  .lockup--dark .lockup__name { color: var(--brand-grey); }

  .person__name {
    position: absolute;
    color: var(--brand-blue);
    font-size: 15.5px;
    letter-spacing: 0.3px;
    text-transform: uppercase;
  }
  .person__role, .contact {
    position: absolute;
    color: var(--brand-grey);
    font-size: 10px;
    line-height: 12px;
  }
  .contact__label { color: var(--brand-blue); }
  .contact__web { color: var(--brand-blue); }
  .contact--lines { line-height: 13.5px; }

  .rule-bar { position: absolute; left: 0; bottom: 0; height: 8px; }
  .rule-bar--blue { width: 235px; background: var(--brand-blue); }
  .rule-bar--grey { left: 235px; width: 165px; background: var(--brand-grey); }

  .divider { position: absolute; width: 1px; background: var(--brand-grey); }
  .swoosh { position: absolute; left: 0; top: 0; }
</style>
</head>
<body>

  <!-- Back, plain -->
  <section class="card card--back card--back-plain">
    <div class="lockup lockup--light" style="left:60px; top:176px;">
      <span class="lockup__dot"></span>
      <p class="lockup__name">Holloway<br>Meridian<br>Advisory Pty Ltd</p>
    </div>
  </section>

  <!-- Front, plain -->
  <section class="card card--front card--front-plain">
    <div class="lockup lockup--dark" style="left:118px; top:51px;">
      <span class="lockup__dot"></span>
      <p class="lockup__name">Holloway<br>Meridian<br>Advisory Pty Ltd</p>
    </div>
    <h2 class="person__name" style="left:40px; top:134px;">Nadia Whitcombe</h2>
    <p class="person__role" style="left:40px; top:153px;">Accountant / Company Secretary</p>
    <p class="contact contact--lines" style="left:40px; top:178px;">
      <span class="contact__label">P</span> 0458213907<br>
      <span class="contact__label">E</span> nadia@youremailaddress.com<br>
      <span class="contact__web">www.yourwebaddress.com</span>
    </p>
    <p class="contact contact--lines" style="left:235px; top:192px;">
      PO Box XXXX Harbourview East<br>QLD XXXX
    </p>
    <span class="rule-bar rule-bar--blue"></span>
    <span class="rule-bar rule-bar--grey"></span>
  </section>

  <!-- Back, with band -->
  <section class="card card--back card--back-swoosh">
    <div class="lockup lockup--light" style="left:48px; top:181px;">
      <span class="lockup__dot"></span>
      <p class="lockup__name">Holloway<br>Meridian<br>Advisory Pty Ltd</p>
    </div>
  </section>

  <!-- Front, with swoosh -->
  <section class="card card--front card--front-swoosh">
    <svg class="swoosh" width="400" height="241" viewBox="0 0 400 241" aria-hidden="true">
      <rect x="0" y="0" width="400" height="8" fill="var(--brand-blue)"/>
      <path d="M400 0 L400 8 C300 10 120 20 40 55 C0 75 10 110 60 125 C100 137 150 143 180 145 C120 145 40 130 18 105 C-5 80 15 50 70 30 C150 5 300 0 400 0 Z" fill="var(--brand-blue)"/>
    </svg>
    <div class="lockup lockup--dark" style="left:118px; top:60px;">
      <span class="lockup__dot"></span>
      <p class="lockup__name">Holloway<br>Meridian<br>Advisory Pty Ltd</p>
    </div>
    <h2 class="person__name" style="left:40px; top:166px;">Nadia Whitcombe</h2>
    <p class="person__role" style="left:40px; top:184px; line-height:11.5px;">
      Accountant / Company Secretary<br>Director of the company
    </p>
    <span class="divider" style="left:210px; top:155px; height:66px;"></span>
    <p class="contact" style="left:221px; top:153px;">
      <span class="contact__label">P</span> 0458213907<br>
      <span class="contact__label">E</span> nadia@youremailaddress.com<br>
      <span class="contact__web">www.yourwebaddress.com</span>
    </p>
    <p class="contact" style="left:221px; top:199px;">
      PO Box XXXX Harbourview East<br>QLD XXXX
    </p>
  </section>

</body>
</html>
```